Flyer Vacation Gift Certificate

I need to create a beautiful flyer 8.5 x 11 PDF format flyer design. <br/><br/>Instructions:<br/>The flyer will really be a gift voucher for a las vegas vacation getaway. So must have a Las Vegas Theme exciting fun<br/><br/>The voucher should have two modules that will be editable. <br/>Must have a "Compliments Of" area and also must have an "Exclusively For" area<br/><br/>Keep in mind that this flyer will be printed so keep that in mind :)<br/><br/>Here the is the content for the vacation voucher:<br/><br/>There is no doubt that Las Vegas is one of the hottest travel destinations around the world. In fact, some people would even go as far as<br/>saying that perhaps it is THE hottest place to visit. Enjoy up to 4 nights of resort/casino accommodations in exciting Las Vegas, NV. Millions of people travel to this exciting city each year to enjoy its thrills. Thanks to the business you received this certificate from, now you can enjoy exciting Las Vegas, NV too!<br/><br/>Features:<br/>*Travel 7 Days A Week<br/>*Stay Your Choice Of Nights (1-4 Nights)<br/>*Good For Two Adults & Two Children<br/>*Pay Just The Taxes & Fees<br/>*Multiple Travel Date Requests Allowed<br/>*Fully Transferable To Another Person<br/>*Just A 30 Days Advance Notice Required<br/>*You Will Have 12 Months To Complete Travel After Redemption<br/><br/>HOW CAN WE DO THIS?<br/><br/>We contract with the world leading hotel chains and resorts to help them fill their otherwise empty rooms.<br/><br/>We help fill empty rooms which the hotels, resorts and cruise lines turn into additional revenue from other areas of their property and future bookings.<br/><br/>Hotels rarely experience full occupancy, yet they remain open, providing rooms and services at fixed costs. So when hotels give out their rooms by partnering with marketing companies like us, they might miss out on the room fee, but they already didn't have that in the first place, at least now they have the opportunity to gain a customer for their in-house restaurants, room service, their casinos, an extra day stay, future bookings, etc.<br/><br/>VIEW ALL THE DETAILS OF THIS SPECIAL OFFER AND REDEEM ONLINE AT <br/>WWW.TOPAZVOUCHERDESK.COM<br/><br/>Certificate ID # 47261-38504<br/>Expires 02/29/2020<br/><br/><br/>*terms and conditions apply see website for details<br/><br/>KEEP IN MIND THE EXAMPLES I AM UPLOADING ARE SIMPLY TO SHOW YOU THAT THEY CONTAIN THE "COMPLIMENTS OF" AND "EXCLUSIVELY FOR" ELEMENTS. THESE MUST BE INCLUDED IN NEW DESIGN. PLEASE ONLY USE THE CONTENT I PROVIDED IN BRIEF, DONT USE CONTENT FROM EXAMPLES.

Target Market(s)

CONSUMERS THAT HAVE BEEN REWARDED WITH A VACATION CERTIFICATE FOR DOING BUSINESS WITH A COMPANY.

COMPANIES USE THESE AS MARKETING INCENTIVES TO ATTRACT MORE CUSTOMERS AND TO REWARD LOYALTY, ETC.

Industry/Entity Type

Travel Industry

Colors

Designer to choose colors to be used in the design.

Requirements
Must have
• I need to create a beautiful flyer 8.5 x 11 PDF format flyer design.
• Instructions:
• The flyer will really be a gift voucher for a las vegas vacation getaway. So must have a Las Vegas Theme exciting fun
• The voucher should have two modules that will be editable.
• Must have a "Compliments Of" area and also must have an "Exclusively For" area
• Keep in mind that this flyer will be printed so keep that in mind :)
• Here the is the content for the vacation voucher:
• There is no doubt that Las Vegas is one of the hottest travel destinations around the world. In fact, some people would even go as far as
• saying that perhaps it is THE hottest place to visit. Enjoy up to 4 nights of resort/casino accommodations in exciting Las Vegas, NV. Millions of people travel to this exciting city each year to enjoy its thrills. Thanks to the business you received this certificate from, now you can enjoy exciting Las Vegas, NV too!
• Features:
• *Travel 7 Days A Week
• *Stay Your Choice Of Nights (1-4 Nights)
• *Good For Two Adults & Two Children
• *Pay Just The Taxes & Fees
• *Multiple Travel Date Requests Allowed
• *Fully Transferable To Another Person
• *Just A 30 Days Advance Notice Required
• *You Will Have 12 Months To Complete Travel After Redemption
• HOW CAN WE DO THIS?
• We contract with the world leading hotel chains and resorts to help them fill their otherwise empty rooms.
• We help fill empty rooms which the hotels, resorts and cruise lines turn into additional revenue from other areas of their property and future bookings.
• Hotels rarely experience full occupancy, yet they remain open, providing rooms and services at fixed costs. So when hotels give out their rooms by partnering with marketing companies like us, they might miss out on the room fee, but they already didn't have that in the first place, at least now they have the opportunity to gain a customer for their in-house restaurants, room service, their casinos, an extra day stay, future bookings, etc.
• VIEW ALL THE DETAILS OF THIS SPECIAL OFFER AND REDEEM ONLINE AT
• WWW.TOPAZVOUCHERDESK.COM
• Certificate ID # 47261-38504
• Expires 02/29/2020
• *terms and conditions apply see website for details
• KEEP IN MIND THE EXAMPLES I AM UPLOADING ARE SIMPLY TO SHOW YOU THAT THEY CONTAIN THE "COMPLIMENTS OF" AND "EXCLUSIVELY FOR" ELEMENTS. THESE MUST BE INCLUDED IN NEW DESIGN. PLEASE ONLY USE THE CONTENT I PROVIDED IN BRIEF, DONT USE CONTENT FROM EXAMPLES.
Nice to have
• EXCITING LAS VEGAS IMAGES THAT MAKE SOMEONE WANT TO GO THERE

```html
<!DOCTYPE html>
<html lang="en">
<head>
<meta charset="utf-8">
<title>Las Vegas Vacation Gift Certificate</title>
<link href="https://fonts.googleapis.com/css2?family=Barlow+Condensed:ital,wght@0,500;0,600;0,700;1,500&family=PT+Sans:wght@400&family=PT+Sans+Narrow:wght@400;700&display=swap" rel="stylesheet">
<style>
  :root {
    --stage: #676767;
    --navy: #0f4f82;
    --deep-blue: #145a8a;
    --teal: #3f8a96;
    --sage: #8fb3a3;
    --gold: #e8dfaa;
    --cream: #f2ecbf;
    --ink: #111820;
    --panel: #f3f3f3;
    --white: #ffffff;
  }
  * { margin: 0; padding: 0; box-sizing: border-box; }
  html, body { width: 1200px; height: 1200px; overflow: hidden; }
  body { background: var(--stage); position: relative; font-family: "PT Sans Narrow", sans-serif; }

  .page {
    position: absolute; top: 249px; width: 547px; height: 702px;
    background: var(--white); overflow: hidden;
    box-shadow: 8px 8px 6px rgba(0,0,0,.35);
  }
  .page--front { left: 37px; }
  .page--back { left: 619px; }
  .page svg.backdrop { position: absolute; inset: 0; width: 547px; height: 702px; }

  /* front */
  .intro-rule { position: absolute; left: 18px; top: 526px; width: 75px; height: 3px; background: var(--navy); }
  .intro-headline {
    position: absolute; left: 18px; top: 538px; width: 320px;
    font-family: "Barlow Condensed", sans-serif; font-style: italic; font-weight: 500;
    font-size: 15.5px; line-height: 16.6px; color: var(--ink);
  }
  .intro-body {
    position: absolute; left: 16px; top: 619px; width: 512px;
    font-family: "PT Sans", sans-serif; font-size: 8.4px; line-height: 10.4px; color: var(--ink);
  }

  .redeem-band {
    position: absolute; left: 0; bottom: 0; width: 547px; height: 38px;
    background: linear-gradient(90deg, var(--gold) 0%, var(--teal) 12%, var(--navy) 30%, var(--navy) 72%, var(--teal) 88%, var(--gold) 100%);
    display: flex; align-items: center; justify-content: center;
    font-family: "Barlow Condensed", sans-serif; font-weight: 600; font-size: 10.5px; color: var(--white); letter-spacing: .1px;
  }
  .redeem-band strong { font-weight: 700; margin-left: 4px; }

  /* back */
  .ribbon {
    position: absolute; left: 50%; transform: translateX(-50%);
    height: 26px; display: flex; align-items: center; justify-content: center;
    background: var(--gold);
    clip-path: polygon(0 0, 100% 0, 94% 50%, 100% 100%, 0 100%, 6% 50%);
    font-family: "Barlow Condensed", sans-serif; font-weight: 700; font-size: 17px; color: var(--ink);
  }
  .ribbon--features { top: 21px; width: 140px; }
  .ribbon--how { top: 137px; width: 256px; clip-path: polygon(0 0, 100% 0, 97% 50%, 100% 100%, 0 100%, 3% 50%); }

  .feature-list { position: absolute; top: 60px; list-style: none; color: var(--white); font-size: 9.6px; line-height: 15.6px; }
  .feature-list li { position: relative; padding-left: 11px; }
  .feature-list li::before { content: ""; position: absolute; left: 0; top: 5px; width: 5px; height: 5px; border-radius: 50%; background: var(--white); }
  .feature-list li.continued::before { display: none; }
  .feature-list--a { left: 17px; }
  .feature-list--b { left: 195px; }
  .feature-list--c { left: 367px; }

  .how-list { position: absolute; left: 17px; top: 177px; width: 518px; list-style: none; color: var(--white); font-size: 9px; line-height: 10.4px; }
  .how-list li { position: relative; padding-left: 11px; margin-bottom: 5px; }
  .how-list li::before { content: ""; position: absolute; left: 0; top: 3px; width: 5px; height: 5px; border-radius: 50%; background: var(--white); }

  .spot { position: absolute; width: 140px; height: 150px; }
  .spot svg { width: 140px; height: 150px; }
  .spot__label {
    position: absolute; left: 12px; top: 113px; width: 116px; height: 22px;
    display: flex; align-items: center; justify-content: center;
    background: var(--deep-blue); color: var(--white);
    font-family: "Barlow Condensed", sans-serif; font-weight: 600; font-size: 11px;
    clip-path: polygon(0 0, 100% 0, 93% 100%, 7% 100%);
  }
  .spot--strip { left: 48px; top: 278px; }
  .spot--sign { left: 204px; top: 298px; }
  .spot--skyline { left: 361px; top: 278px; }

  .module-title {
    position: absolute; top: 469px; width: 254px; text-align: center;
    font-family: "Barlow Condensed", sans-serif; font-weight: 700; font-size: 15px; color: var(--deep-blue); letter-spacing: .3px;
  }
  .module-title--from { left: 15px; }
  .module-title--for { left: 277px; }
  .module-box { position: absolute; top: 492px; width: 254px; height: 137px; background: var(--panel); border-radius: 6px; }
  .module--from { left: 15px; }
  .module--for { left: 277px; }

  .cert-line {
    position: absolute; left: 19px; right: 19px; top: 647px;
    display: flex; justify-content: space-between; align-items: baseline;
    font-family: "Barlow Condensed", sans-serif; font-weight: 600; font-size: 13px; color: var(--ink);
    font-variant-ligatures: none;
  }
  .cert-line .terms { font-family: "PT Sans Narrow", sans-serif; font-weight: 400; font-size: 7.5px; color: #333; }
</style>
</head>
<body>

<section class="page page--front" aria-label="Certificate front">
  <svg class="backdrop" viewBox="0 0 547 702">
    <defs>
      <linearGradient id="cityTones" x1="0" y1="0" x2="0" y2="1">
        <stop offset="0" stop-color="#f3e7cf"/>
        <stop offset=".2" stop-color="#f1cf95"/>
        <stop offset=".42" stop-color="#c9a37c"/>
        <stop offset=".6" stop-color="#9a9aa0"/>
        <stop offset=".78" stop-color="#5fb0c6"/>
        <stop offset="1" stop-color="#4f8f74"/>
      </linearGradient>
      <linearGradient id="gardenTones" x1="0" y1="0" x2="1" y2="1">
        <stop offset="0" stop-color="#6f8d6a"/>
        <stop offset=".45" stop-color="#4a7a3a"/>
        <stop offset=".75" stop-color="#b78a70"/>
        <stop offset="1" stop-color="#2f5a2a"/>
      </linearGradient>
      <linearGradient id="cornerTeal" x1="0" y1="0" x2="1" y2="1">
        <stop offset="0" stop-color="#2f7d8e"/>
        <stop offset="1" stop-color="#9fbf9a"/>
      </linearGradient>
      <linearGradient id="sideBlue" x1="0" y1="0" x2="1" y2="0">
        <stop offset="0" stop-color="#3f8a96"/>
        <stop offset="1" stop-color="#0f4f82"/>
      </linearGradient>
    </defs>

    <path role="img" aria-label="Photo of landscaped resort gardens, trees and roads beside the Strip" d="M0 400 H547 V620 H0 Z" fill="url(#gardenTones)"/>
    <path role="img" aria-label="Photo of the Las Vegas Strip at sunrise with the fountain lake, resort towers and observation wheel" d="M0 0 H547 V400 C470 420 380 432 280 425 C180 420 80 450 0 500 Z" fill="url(#cityTones)"/>

    <path d="M0 0 H140 C80 25 30 60 0 110 Z" fill="url(#cornerTeal)"/>
    <path d="M0 115 C35 60 90 25 168 0" fill="none" stroke="#ffffff" stroke-width="6"/>
    <path d="M0 82 C30 45 70 18 122 0" fill="none" stroke="#ffffff" stroke-width="3"/>

    <path d="M547 270 C520 330 470 380 390 412 C460 410 520 395 547 380 Z" fill="url(#sideBlue)"/>
    <path d="M547 300 C505 370 430 408 320 424" fill="none" stroke="#ffffff" stroke-width="3"/>
    <path d="M547 395 C470 420 380 436 260 432 C150 430 70 455 0 500" fill="none" stroke="#ffffff" stroke-width="7"/>
    <path d="M0 470 C60 440 120 430 190 432" fill="none" stroke="#ffffff" stroke-width="2.5"/>

    <path d="M0 486 C90 448 190 462 290 525 C370 575 450 606 547 606 L547 702 L0 702 Z" fill="#ffffff"/>
  </svg>

  <div class="intro-rule"></div>
  <p class="intro-headline">There is no doubt that Las Vegas<br>is one of the hottest travel destinations<br>around the world. In fact, some people would even<br>go as far as</p>
  <p class="intro-body">saying that perhaps it is THE hottest place to visit. Enjoy up to 4 nights of resort/casino accommodations in exciting Las Vegas, NV.<br>Millions of people travel to this exciting city each year to enjoy its thrills. Thanks to the business you received this certificate from, now<br>you can enjoy exciting Las Vegas, NV too!</p>

  <div class="redeem-band">VIEW ALL THE DETAILS OF THIS SPECIAL OFFER AND REDEEM ONLINE AT <strong>WWW.TOPAZVOUCHERDESK.COM</strong></div>
</section>

<section class="page page--back" aria-label="Certificate back">
  <svg class="backdrop" viewBox="0 0 547 702">
    <defs>
      <linearGradient id="backWash" x1="0" y1="1" x2="1" y2="0">
        <stop offset="0" stop-color="#9fb89a"/>
        <stop offset=".35" stop-color="#3f8a96"/>
        <stop offset=".75" stop-color="#185f8c"/>
        <stop offset="1" stop-color="#0f4f82"/>
      </linearGradient>
    </defs>
    <path d="M0 0 H547 V287 C470 340 380 367 274 367 C170 367 80 340 0 295 Z" fill="url(#backWash)"/>
  </svg>

  <div class="ribbon ribbon--features">FEATURES:</div>
  <ul class="feature-list feature-list--a">
    <li>Travel 7 Days A Week</li>
    <li>Stay Your Choice Of Nights (1-4 Nights)</li>
    <li>Good For Two Adults &amp; Two Children</li>
  </ul>
  <ul class="feature-list feature-list--b">
    <li>Pay Just The Taxes &amp; Fees</li>
    <li>Multiple Travel Date Requests Allowed</li>
    <li>Fully Transferable To Another Person</li>
  </ul>
  <ul class="feature-list feature-list--c">
    <li>Just A 30 Days Advance Notice Required</li>
    <li>You Will Have 12 Months To Complete</li>
    <li class="continued">Travel After Redemption</li>
  </ul>

  <div class="ribbon ribbon--how">HOW CAN WE DO THIS?</div>
  <ul class="how-list">
    <li>We contract with the world leading hotel chains and resorts to help them fill their otherwise empty rooms.</li>
    <li>We help fill empty rooms which the hotels, resorts and cruise lines turn into additional revenue from other areas of their property and future bookings.</li>
    <li>Hotels rarely experience full occupancy, yet they remain open, providing rooms and services at fixed costs. So when hotels give out their rooms by partnering with marketing companies like us, they might miss out on the room fee, but they already didn't have that in the first place, at least now they have the opportunity to gain a customer for their in-house restaurants, room service, their casinos, an extra day stay, future bookings, etc.</li>
  </ul>

  <div class="spot spot--strip">
    <svg viewBox="0 0 140 150">
      <defs><linearGradient id="stripNight" x1="0" y1="0" x2="0" y2="1"><stop offset="0" stop-color="#1b2a6b"/><stop offset=".6" stop-color="#5a4aa8"/><stop offset="1" stop-color="#c8503a"/></linearGradient></defs>
      <circle cx="70" cy="70" r="69" fill="#0f4f82"/>
      <circle cx="70" cy="70" r="65" fill="#ffffff"/>
      <circle role="img" aria-label="Photo of the Las Vegas Boulevard casinos lit up at night" cx="70" cy="70" r="62" fill="url(#stripNight)"/>
    </svg>
    <div class="spot__label">Boulevard in Clark County</div>
  </div>
  <div class="spot spot--sign">
    <svg viewBox="0 0 140 150">
      <defs><linearGradient id="signDay" x1="0" y1="0" x2="0" y2="1"><stop offset="0" stop-color="#2f6fc4"/><stop offset=".6" stop-color="#7fb0e6"/><stop offset="1" stop-color="#3a4a3a"/></linearGradient></defs>
      <circle cx="70" cy="70" r="69" fill="#0f4f82"/>
      <circle cx="70" cy="70" r="65" fill="#ffffff"/>
      <circle role="img" aria-label="Photo of the classic Las Vegas welcome sign under a blue sky with palm trees" cx="70" cy="70" r="62" fill="url(#signDay)"/>
    </svg>
    <div class="spot__label">las vegas nevada</div>
  </div>
  <div class="spot spot--skyline">
    <svg viewBox="0 0 140 150">
      <defs><linearGradient id="skylineDusk" x1="0" y1="0" x2="0" y2="1"><stop offset="0" stop-color="#b8c6dc"/><stop offset=".45" stop-color="#8a7a88"/><stop offset="1" stop-color="#6a5a4c"/></linearGradient></defs>
      <circle cx="70" cy="70" r="69" fill="#0f4f82"/>
      <circle cx="70" cy="70" r="65" fill="#ffffff"/>
      <circle role="img" aria-label="Photo of the downtown Las Vegas skyline and tower in front of desert mountains" cx="70" cy="70" r="62" fill="url(#skylineDusk)"/>
    </svg>
    <div class="spot__label">downtown skyline</div>
  </div>

  <h2 class="module-title module-title--from">COMPLIMENTS OF</h2>
  <h2 class="module-title module-title--for">EXCLUSIVELY FOR</h2>
  <div class="module-box module--from" aria-label="Compliments of area"></div>
  <div class="module-box module--for" aria-label="Exclusively for area"></div>

  <div class="cert-line">
    <span>Certificate ID # 47261-38504</span>
    <span class="terms">*terms and conditions apply see website for details</span>
    <span>Expires 02/29/2020</span>
  </div>

  <div class="redeem-band">VIEW ALL THE DETAILS OF THIS SPECIAL OFFER AND REDEEM ONLINE AT <strong>WWW.TOPAZVOUCHERDESK.COM</strong></div>
</section>

</body>
</html>
```